Elegant Business Cards & Letterhead

We will need the following that need to be designed: Letterhead and Business Cards, there winer will be re-hired for the balance of our stationary needs. Text for the cards and letterheads:

- Corporate Card instead of name
- landline: +971 (4) 362 7041
- mobile: +971 56 2819 605
- 800VELMORA
- email: dubai@velmora-lune.com
- www.velmora-lune.com
- PO Box 387261
Address: Castellan Heights Suite 1708, Dubai UAE

Thank you

Target Market(s)

VIPs, HNWI, High-end Families.

Industry/Entity Type

Luxury Market

Font styles to use
Other font styles liked:
• as explained

Colors

Designer to choose only greyscale colors for use in the design.

Requirements
Must have
• Elegant, Simple, Luxurious, Minimalistic
Nice to have
• Luxury, Golds, Engravings,
Should not have
• Much colors, funky,

```html
<!DOCTYPE html>
<html lang="en">
<head>
<meta charset="utf-8">
<title>Velmora Lune — Stationery</title>
<link href="https://fonts.googleapis.com/css2?family=Cinzel:wght@500&family=Montserrat:wght@400;500&family=Cormorant+Garamond:wght@400;500&display=swap" rel="stylesheet">
<style>
  :root {
    --bg: #ececec;
    --black: #0d0d0d;
    --charcoal: #1c1c1c;
    --graphite: #2e2e2e;
    --gold: #c9a55a;
    --gold-light: #e6cb8c;
    --paper: #ffffff;
    --ink: #4a4a4a;
    --footer-text: #d8d8d8;
  }
  * { margin: 0; padding: 0; box-sizing: border-box; }
  html, body { width: 900px; height: 1200px; overflow: hidden; }
  body { background: var(--bg); position: relative; font-family: "Montserrat", sans-serif; }

  .brand-name {
    font-family: "Cinzel", serif;
    font-weight: 500;
    letter-spacing: 0.08em;
    color: var(--gold);
    white-space: nowrap;
  }

  /* Business cards */
  .card {
    position: absolute;
    width: 440px; height: 252px;
    border-radius: 10px;
    background: linear-gradient(135deg, var(--charcoal), var(--black) 60%);
    box-shadow: 0 10px 24px rgba(0,0,0,.25);
    overflow: hidden;
  }
  .card--front { left: 40px; top: 40px; }
  .card--back { left: 420px; top: 300px; }

  .card__ornament {
    position: absolute;
    background: linear-gradient(160deg, var(--graphite), #141414);
  }
  .card--front .card__ornament {
    left: 0; bottom: 0; width: 150px; height: 150px;
    border-top-right-radius: 60% 55%;
  }
  .card--back .card__ornament {
    right: 0; top: 0; width: 120px; height: 252px;
    border-top-left-radius: 70% 40%;
    border-bottom-left-radius: 40% 30%;
  }

  .card--front .brand-name {
    position: absolute; left: 176px; top: 86px; font-size: 24px;
  }

  .card--back .brand-name {
    position: absolute; left: 30px; top: 28px; font-size: 20px;
  }
  .contact-list {
    position: absolute; left: 30px; top: 78px;
    list-style: none;
  }
  .contact-list li {
    display: flex; align-items: center; gap: 10px;
    font-size: 10.5px; line-height: 19px;
    color: var(--gold-light); letter-spacing: 0.02em;
    white-space: nowrap;
  }
  .contact-list svg { width: 11px; height: 11px; flex: none; }

  /* Letterhead */
  .letterhead {
    position: absolute; left: 245px; top: 580px;
    width: 410px; height: 580px;
    background: var(--paper);
    box-shadow: 0 8px 22px rgba(0,0,0,.18);
    overflow: hidden;
  }
  .letterhead__band { position: absolute; left: 0; width: 410px; }
  .letterhead__band--top { top: 0; height: 70px; }
  .letterhead__band--bottom { bottom: 0; height: 80px; }

  .letterhead .brand-name {
    position: absolute; left: 28px; top: 60px; font-size: 14px;
  }
  .letter-body {
    position: absolute; left: 28px; right: 28px; top: 104px;
    font-family: "Cormorant Garamond", serif;
    font-size: 10.5px; line-height: 1.55; color: var(--ink);
  }
  .letter-body p { margin-bottom: 9px; text-align: justify; }
  .letter-body .sign-off { margin-top: 18px; }
  .letter-body .signatory { margin-top: 34px; font-weight: 500; color: var(--black); }

  .letter-footer {
    position: absolute; left: 0; right: 0; bottom: 12px;
    display: flex; justify-content: center; gap: 14px;
    font-size: 6.5px; color: var(--footer-text); letter-spacing: 0.03em;
    white-space: nowrap;
  }
  .letter-footer span { color: var(--gold-light); }
</style>
</head>
<body>

  <section class="card card--front" aria-label="Business card front">
    <div class="card__ornament" role="img" aria-label="Laser-cut floral filigree ornament in the lower left corner"></div>
    <div class="brand-name">VELMORA LUNE</div>
  </section>

  <section class="card card--back" aria-label="Business card back">
    <div class="card__ornament" role="img" aria-label="Laser-cut floral filigree ornament along the right edge"></div>
    <div class="brand-name">VELMORA LUNE</div>
    <ul class="contact-list">
      <li><svg viewBox="0 0 12 12"><path d="M2.5 1h2l1 3-1.5 1a6 6 0 0 0 3 3l1-1.5 3 1v2a1 1 0 0 1-1 1A9.5 9.5 0 0 1 1.5 2a1 1 0 0 1 1-1z" fill="var(--gold)"/></svg>+971 (4) 362 7041</li>
      <li><svg viewBox="0 0 12 12"><rect x="3" y="0.5" width="6" height="11" rx="1" fill="none" stroke="var(--gold)"/><circle cx="6" cy="9.5" r=".7" fill="var(--gold)"/></svg>+971 56 2819 605</li>
      <li><svg viewBox="0 0 12 12"><circle cx="6" cy="6" r="5" fill="none" stroke="var(--gold)"/><path d="M4 6h4M6 4v4" stroke="var(--gold)"/></svg>800VELMORA</li>
      <li><svg viewBox="0 0 12 12"><rect x="0.5" y="2.5" width="11" height="7" fill="none" stroke="var(--gold)"/><path d="M.5 2.5 6 7l5.5-4.5" fill="none" stroke="var(--gold)"/></svg>dubai@velmora-lune.com</li>
      <li><svg viewBox="0 0 12 12"><circle cx="6" cy="6" r="5" fill="none" stroke="var(--gold)"/><ellipse cx="6" cy="6" rx="2.2" ry="5" fill="none" stroke="var(--gold)"/><path d="M1 6h10" stroke="var(--gold)"/></svg>www.velmora-lune.com</li>
      <li><svg viewBox="0 0 12 12"><rect x="1" y="3" width="10" height="7" fill="none" stroke="var(--gold)"/><path d="M4 3V1.5h4V3" fill="none" stroke="var(--gold)"/></svg>PO Box 387261</li>
      <li><svg viewBox="0 0 12 12"><path d="M6 11.5S2 7 2 4.5a4 4 0 0 1 8 0C10 7 6 11.5 6 11.5z" fill="var(--gold)"/><circle cx="6" cy="4.5" r="1.4" fill="var(--black)"/></svg>Castellan Heights Suite 1708, Dubai UAE</li>
    </ul>
  </section>

  <article class="letterhead" aria-label="Letterhead">
    <svg class="letterhead__band letterhead__band--top" viewBox="0 0 410 70" preserveAspectRatio="none">
      <path d="M0 0H410V22C300 50 150 18 0 42Z" fill="var(--black)"/>
      <path d="M0 46C150 22 300 54 410 26" fill="none" stroke="var(--gold)" stroke-width="2"/>
    </svg>
    <div class="brand-name">VELMORA LUNE</div>

    <div class="letter-body">
      <p>Dear Guest,</p>
      <p>Thank you for your continued trust in our household services. We are pleased to confirm the details of your upcoming placement and the arrangements agreed with our team.</p>
      <p>Each member of staff has been carefully selected, trained and vetted to meet the standards expected by discerning families. Should you require any changes, our concierge is available at all hours.</p>
      <p>We look forward to serving you and your family in the months ahead.</p>
      <p class="sign-off">Kind regards,</p>
      <p class="signatory">Client Relations</p>
    </div>

    <svg class="letterhead__band letterhead__band--bottom" viewBox="0 0 410 80" preserveAspectRatio="none">
      <path d="M0 80H410V26C300 4 140 46 0 20Z" fill="var(--black)"/>
      <path d="M0 15C140 42 300 0 410 21" fill="none" stroke="var(--gold)" stroke-width="2"/>
    </svg>
    <div class="letter-footer">
      <div><span>T</span> +971 (4) 362 7041</div>
      <div><span>E</span> dubai@velmora-lune.com</div>
      <div><span>W</span> www.velmora-lune.com</div>
      <div>PO Box 387261, Dubai UAE</div>
    </div>
  </article>

</body>
</html>
```